Packaging design for handmade soap

We are looking for a packaging design for a brand new product line: handmade soaps, called BRIVO

We are looking for a design of an outer box together with the logo. We need the design for a 90x65x30mm box (see attached). We trying to get a high-end product preferable with vintage elements (but we don't want a shiny box, it will be finished with matte lacque, however logo or other certain elements could be shiny).

The design should reflect the fact that we have a handmade, all natural soap.

I uploaded a couple of packaging examples I like.

UPDATE 1: It also should have a title, which describes the product more accurate, like "Natural Soap with Seabuckthorn and Olive oil"

UPDATE 2: I would remove the expression "high-end" from the description if high end would mean a lot of flowers in the background. I would like if you would insist about the ideea of "natural" in your works

UPDATE 3: Prefered colors green and brown (which brings the ideea of nature, natural)

Target Market(s)

Women 20-45 years with above average income

Industry/Entity Type

Cosmetics

Font styles to use
Serif

Colors
9bcb3c
acd036
cadf82
f78f20
ffc214
f37122
fbed22
fece3e
faa54b

Requirements
Must have
• A literal representation of the brand BRIVO (we don't have a logo for it)

```html
<!DOCTYPE html>
<html lang="en">
<head>
<meta charset="utf-8">
<title>BRIVO Natural Soap – Box Front</title>
<link rel="stylesheet" href="https://fonts.googleapis.com/css2?family=Cinzel:wght@700&family=Sorts+Mill+Goudy&display=swap">
<style>
  :root {
    --page: #ffffff;
    --kraft: #bead7b;
    --kraft-edge: #a8966a;
    --ink: #3a2e1f;
    --ink-soft: #4a3d2a;
    --coral: #cd6857;
    --coral-tint: rgba(214, 110, 92, 0.16);
    --coral-line: rgba(205, 104, 87, 0.75);
    --emboss-light: rgba(255, 244, 214, 0.55);
    --emboss-dark: rgba(40, 28, 12, 0.45);
    --ribbon-text: #cdb384;
  }
  * { margin: 0; padding: 0; box-sizing: border-box; }
  html, body { width: 1200px; height: 902px; overflow: hidden; background: var(--page); }
  .canvas { position: relative; width: 1200px; height: 902px; }

  .box-front {
    position: absolute; left: 170px; top: 163px; width: 834px; height: 595px;
    background: var(--kraft);
    border-left: 2px solid var(--kraft-edge);
    box-shadow: inset 0 0 4px rgba(90, 70, 40, 0.35);
  }

  .ornament {
    position: absolute;
    background: var(--coral-tint);
    border: 1.5px solid var(--coral-line);
  }
  .ornament--tl { left: 12px;  top: 10px;    width: 230px; height: 210px; border-radius: 6px 60% 6px 60%; }
  .ornament--tr { right: 22px; top: 10px;    width: 230px; height: 210px; border-radius: 60% 6px 60% 6px; }
  .ornament--bl { left: 12px;  bottom: 14px; width: 230px; height: 210px; border-radius: 60% 6px 60% 6px; }
  .ornament--br { right: 22px; bottom: 14px; width: 230px; height: 210px; border-radius: 6px 60% 6px 60%; }
  .ornament--ml { left: 10px;  top: 268px; width: 64px; height: 46px; border-radius: 50%; }
  .ornament--mr { right: 10px; top: 268px; width: 64px; height: 46px; border-radius: 50%; }

  .brand-name {
    position: absolute; left: 0; right: 0; top: 58px;
    text-align: center;
    font-family: "Sorts Mill Goudy", serif;
    font-size: 86px; letter-spacing: 6px;
    color: var(--ink);
  }

  .product-title {
    position: absolute; left: 0; right: 0; top: 248px;
    text-align: center;
    font-family: "Cinzel", serif; font-weight: 700;
    font-size: 56px; letter-spacing: 2px;
    color: var(--ink);
    text-shadow: -1px -1px 0 var(--emboss-light), 2px 2px 2px var(--emboss-dark);
  }

  .ribbon { position: absolute; left: 170px; top: 330px; width: 496px; height: 52px; }
  .ribbon-label {
    position: absolute; left: 170px; top: 330px; width: 496px; height: 52px;
    display: flex; align-items: center; justify-content: center;
    font-family: "Cinzel", serif; font-weight: 700;
    font-size: 30px; letter-spacing: 17px; padding-left: 17px;
    color: var(--ribbon-text);
    text-shadow: 1px 1px 1px rgba(90, 40, 30, 0.4);
  }

  .ingredients {
    position: absolute; left: 0; right: 0; top: 398px;
    text-align: center;
    font-family: "Sorts Mill Goudy", serif;
    font-size: 37px; color: var(--ink-soft);
    text-shadow: -1px -1px 0 var(--emboss-light), 1px 1px 1px var(--emboss-dark);
  }

  .net-weight {
    position: absolute; left: 0; right: 0; top: 518px;
    text-align: center;
    font-family: "Sorts Mill Goudy", serif;
    font-size: 37px; letter-spacing: 1px; word-spacing: 2px;
    color: var(--ink-soft);
    text-shadow: -1px -1px 0 var(--emboss-light), 1px 1px 1px var(--emboss-dark);
  }
</style>
</head>
<body>
<div class="canvas">
  <section class="box-front">
    <div class="ornament ornament--tl" role="img" aria-label="Coral floral scroll ornament, top left corner"></div>
    <div class="ornament ornament--tr" role="img" aria-label="Coral floral scroll ornament, top right corner"></div>
    <div class="ornament ornament--bl" role="img" aria-label="Coral floral scroll ornament, bottom left corner"></div>
    <div class="ornament ornament--br" role="img" aria-label="Coral floral scroll ornament, bottom right corner"></div>
    <div class="ornament ornament--ml" role="img" aria-label="Small coral flower rosette"></div>
    <div class="ornament ornament--mr" role="img" aria-label="Small coral flower rosette"></div>

    <div class="brand-name">BRIVO</div>

    <h1 class="product-title">NATURAL SOAP</h1>

    <svg class="ribbon" viewBox="0 0 496 52" aria-hidden="true">
      <polygon points="0,0 496,0 476,26 496,52 0,52 20,26" fill="var(--coral)"/>
    </svg>
    <div class="ribbon-label">HANDMADE</div>

    <p class="ingredients">With Seabuckthorn &amp; Olive oil</p>

    <p class="net-weight">4oz/ 100g</p>
  </section>
</div>
</body>
</html>
```